Public Relations Agency Seeks Wordpress Design and Coding

TORVEX Media is a public relations agency specializing in media relations, public affairs and marketing communication.

The site should display the following visual characteristics: professionalism, trustworthiness, high-tech focus, clear and concise design.

The desired colors are royal blue, gray and hints of red.

Design look/feel inspired by this site: http://brisklanefetes.example/

Specifications:

1. Navigation/Pages/Index:

HOME

ABOUT US

SERVICES

NEWS

CONTACT

---

2. Functionality of/content for each page:

- Home
o Dominant photo (professional, edgy, innovative)
o Simple, straightforward access to/from “Home” from other pages
o Includes logo (attached) and tagline "Unleash the power of communication"
o Direct link to “CONTACT”
o Links to social media accounts: Facebook, Twitter, LinkedIn

- About Us

o Company profile blurb
o President’s photo with short bio

- Services
o Public Relations
 Strategic communication
 Brand and reputation management
 Community relations
o Media Relations
 News coverage and contacts
 Media training and interview skills
 Crisis communications
o Congressional Affairs
 Public affairs
 Public policy
 Legislative strategy
o Mass Communication
 Speechwriting
 Presentation creation
 Social media
o Marketing Communications
 Business collateral material
 Promotional campaigns
 Special events and tradeshows

- News
o Blog-like page to post information and/or share news from other sites

- Contact
o Standard “Contact Us” form (Name, Email, Phone, Message)
o Direct Contact
 (555) 314-2690
 Marlow@TORVEXmedia.example

Target Market(s)

Small to large businesses specializing in high technology, defense/military, medicine/healthcare, and wide array of professional services.

Industry/Entity Type

Marketing

Font styles to use
Serif
Sans Serif

Colors
0555a3
ec2027
edf3f7

Requirements
Must have
• -- Project reqires DESIGN - and - fully CODED.

-- Strong SEO

-- Optimized for mobile viewing

Thank you!

```html
<!DOCTYPE html>
<html lang="en">
<head>
<meta charset="utf-8">
<title>TORVEX Media — Unleash the Power of Communication</title>
<link rel="stylesheet" href="https://fonts.googleapis.com/css2?family=Oswald:wght@400;500&family=Open+Sans:wght@400;600;700&display=swap">
<style>
:root{
  --blue:#0555a3;
  --blue-dark:#0a3f7d;
  --red:#ec2027;
  --mist:#edf3f7;
  --ink:#333a40;
  --grey:#8a8f94;
  --light:#e9ebed;
  --bar:#2a2d30;
  --white:#ffffff;
}
*{box-sizing:border-box;margin:0;padding:0}
html,body{width:1200px;height:2776px;overflow:hidden}
body{position:relative;font-family:"Open Sans",Arial,sans-serif;color:var(--ink);background:var(--white)}
.heading{font-family:"Oswald","Arial Narrow",sans-serif;font-weight:400;text-transform:uppercase;text-align:center}
.btn{display:inline-block;font-family:"Open Sans",Arial,sans-serif;font-weight:700;font-size:13px;text-transform:uppercase;color:var(--white);text-decoration:none;text-align:center}

/* hero */
.hero{position:absolute;left:0;top:0;width:1200px;height:740px;overflow:hidden}
.hero-photo{position:absolute;inset:0;background:linear-gradient(180deg,#cfd3d6 0%,#9a9fa4 25%,#4b4f53 45%,#2d3033 70%,#3a3d40 100%)}
.topbar{position:absolute;left:0;top:0;width:1200px;height:32px;background:var(--bar);display:flex;align-items:center;padding:0 220px}
.topbar .social{display:flex;gap:8px}
.topbar .social span{width:18px;height:18px;border-radius:50%;background:#555b60}
.topbar .phone{margin-left:110px;display:flex;align-items:center;gap:8px;color:#d8dadc;font-size:13px}
.topbar .search{margin-left:auto;width:170px;height:20px;background:#45494d;color:#9a9fa4;font-size:11px;padding:2px 8px}
.masthead{position:absolute;left:0;top:32px;width:1200px;height:170px;background:rgba(255,255,255,.86);text-align:center}
.logo{margin-top:30px;font-family:"Oswald","Arial Narrow",sans-serif;font-weight:500;font-size:56px;line-height:64px;color:var(--ink);letter-spacing:2px;text-transform:uppercase}
.nav{display:flex;justify-content:center;gap:6px;margin-top:24px}
.nav a{font-size:12px;font-weight:600;color:var(--ink);text-decoration:none;text-transform:uppercase;padding:6px 16px}
.nav a.active{background:var(--white);color:var(--red);border-bottom:2px solid var(--red)}
.hero-copy{position:absolute;left:0;top:400px;width:1200px;text-align:center;color:var(--white)}
.hero-copy h1{font-size:50px;line-height:60px;font-weight:500;color:var(--white)}
.hero-copy p{width:660px;margin:20px auto 0;font-size:15px;line-height:22px}
.hero-copy .btn{margin-top:28px;background:var(--red);padding:12px 40px}
.dots{position:absolute;left:0;top:694px;width:1200px;display:flex;justify-content:center;gap:8px}
.dots span{width:11px;height:11px;border-radius:50%;border:2px solid var(--white)}
.dots span.on{background:var(--white)}

/* about */
.about{position:absolute;left:0;top:740px;width:1200px;height:348px;background:var(--white)}
.about h2{margin-top:36px;font-size:52px;line-height:60px;color:#b9bcbf}
.portrait{position:absolute;left:206px;top:118px;width:148px;height:148px;border-radius:50%;border:6px solid var(--light);background:radial-gradient(circle at 50% 40%,#e0c9a8,#b48a5d 60%,#8d6b49)}
.about p{position:absolute;left:400px;top:112px;width:700px;font-size:15px;line-height:22px;color:var(--grey)}
.about .btn{position:absolute;left:400px;top:236px;background:var(--red);padding:9px 22px;font-size:12px}

/* services */
.services{position:absolute;left:0;top:1088px;width:1200px;height:612px;background:radial-gradient(ellipse at 50% 30%,#1a6cc0 0%,var(--blue) 45%,var(--blue-dark) 100%);color:var(--white)}
.services h2{margin-top:50px;font-size:46px;line-height:56px;color:var(--white)}
.service{position:absolute;top:138px;width:260px;text-align:center}
.service .icon{width:128px;height:128px;margin:0 auto;border-radius:50%;border:3px solid rgba(255,255,255,.85);display:flex;align-items:center;justify-content:center}
.service h3{margin-top:36px;font-size:17px;font-weight:700;text-transform:uppercase}
.service p{margin-top:8px;font-size:14px;line-height:19px;color:#dfe9f4}
.service .btn{margin-top:32px;background:var(--blue-dark);border:1px solid rgba(255,255,255,.3);padding:8px 32px;font-size:11px}

/* news */
.news{position:absolute;left:0;top:1700px;width:1200px;height:460px;background:var(--white)}
.news h2{margin-top:40px;font-size:52px;line-height:60px;color:#b9bcbf}
.post{position:absolute;left:240px;width:720px;height:130px}
.post .thumb{position:absolute;left:0;top:0;width:112px;height:112px;border-radius:50%;border:5px solid var(--light);background:radial-gradient(circle at 50% 40%,#d9c2a2,#8d8f92 65%,#5b5e61)}
.post .body{position:absolute;left:150px;top:4px;width:570px}
.post time{font-size:11px;color:var(--grey)}
.post h4{font-size:14px;font-weight:700;color:var(--red);margin-top:2px}
.post p{font-size:12px;line-height:17px;color:var(--grey);margin-top:2px}
.post .more{font-size:11px;font-weight:700;color:var(--ink);margin-top:4px}
.arrow{position:absolute;top:230px;width:44px;height:44px;border-radius:50%;background:#a9adb1;display:flex;align-items:center;justify-content:center}

/* contact */
.contact{position:absolute;left:0;top:2160px;width:1200px;height:460px;overflow:hidden}
.contact-photo{position:absolute;inset:0;background:linear-gradient(160deg,#3b3f43 0%,#1f2225 45%,#4a4f54 75%,#6a7075 100%)}
.contact h2{position:relative;margin-top:34px;font-size:50px;line-height:60px;color:var(--white)}
.form{position:absolute;left:240px;top:160px;width:720px}
.field{position:absolute;left:0;width:340px;height:44px;background:rgba(10,12,14,.75);color:#9ea3a8;font-size:13px;padding:12px 14px}
.message{position:absolute;left:360px;top:0;width:360px;height:112px;background:rgba(10,12,14,.75);color:#9ea3a8;font-size:13px;padding:12px 14px}
.submit{position:absolute;left:360px;top:136px;width:360px;height:44px;background:var(--red);line-height:44px}

/* footer */
.footer{position:absolute;left:0;top:2620px;width:1200px;height:156px;background:var(--light);text-align:center}
.footer nav{margin-top:36px;display:flex;justify-content:center;gap:22px}
.footer nav a{font-size:11px;color:var(--grey);text-decoration:none;text-transform:uppercase}
.footer .copy{margin-top:14px;font-size:11px;color:var(--grey)}
.footer .social{margin-top:16px;display:flex;justify-content:center;gap:8px}
.footer .social span{width:26px;height:26px;border-radius:3px;background:var(--blue)}
</style>
</head>
<body>

<header class="hero">
  <div class="hero-photo" role="img" aria-label="Photo of a team stacking hands together in a huddle"></div>
  <div class="topbar">
    <div class="social"><span></span><span></span><span></span></div>
    <div class="phone">
      <svg width="14" height="14" viewBox="0 0 24 24"><path fill="#d8dadc" d="M6.6 10.8a15 15 0 0 0 6.6 6.6l2.2-2.2a1 1 0 0 1 1-.25 11.4 11.4 0 0 0 3.6.6 1 1 0 0 1 1 1V20a1 1 0 0 1-1 1A17 17 0 0 1 3 4a1 1 0 0 1 1-1h3.5a1 1 0 0 1 1 1c0 1.25.2 2.45.6 3.6a1 1 0 0 1-.25 1z"/></svg>
      (555) 314-2690
    </div>
    <div class="search">Search</div>
  </div>
  <div class="masthead">
    <div class="logo">TORVEX Media</div>
    <nav class="nav">
      <a class="active" href="#">Home</a>
      <a href="#">About Us</a>
      <a href="#">Services</a>
      <a href="#">News</a>
      <a href="#">Contact Us</a>
    </nav>
  </div>
  <div class="hero-copy">
    <h1 class="heading">Unleash the Power of Communication</h1>
    <p>Lorem ipsum dolor sit amet, consectetur adipiscing elit, sed do eiusmod tempor incididunt ut labore et dolore magna aliqua. Ut enim ad minim veniam, quis nostrud exercitation ullamco laboris nisi ut aliquip ex ea commodo consequat. Duis aute irure dolor in reprehenderit velit esse.</p>
    <a class="btn" href="#">Know More</a>
  </div>
  <div class="dots"><span class="on"></span><span></span><span></span><span></span><span></span></div>
</header>

<section class="about">
  <h2 class="heading">About Us</h2>
  <div class="portrait" role="img" aria-label="Portrait photo of the agency president"></div>
  <p>Lorem ipsum dolor sit amet, consectetur adipiscing elit, sed do eiusmod tempor incididunt ut labore et dolore magna aliqua. Ut enim ad minim veniam, quis nostrud exercitation ullamco laboris nisi ut aliquip ex ea commodo consequat. Duis aute irure dolor in reprehenderit in voluptate velit esse cillum dolore eu fugiat nulla pariatur sint occaecat cupidatat.</p>
  <a class="btn" href="#">Read More</a>
</section>

<section class="services">
  <h2 class="heading">We Are Specialize In</h2>

  <article class="service" style="left:130px">
    <div class="icon"><svg width="60" height="60" viewBox="0 0 24 24" fill="none" stroke="#fff" stroke-width="1.6" stroke-linecap="round"><rect x="9" y="3" width="6" height="11" rx="3"/><path d="M6 11a6 6 0 0 0 12 0M12 17v4M9 21h6"/></svg></div>
    <h3>Media Relations</h3>
    <p>Lorem ipsum dolor sit amet, consectetur adipiscing elit, sed do eiusmod tempor incididunt ut labore et dolore magna aliqua enim ad minim veniam.</p>
    <a class="btn" href="#">Know More</a>
  </article>

  <article class="service" style="left:470px">
    <div class="icon"><svg width="64" height="64" viewBox="0 0 24 24" fill="none" stroke="#fff" stroke-width="1.5" stroke-linecap="round"><path d="M7 3h10a2 2 0 0 1 2 2v4a2 2 0 0 1-2 2h-4l-3 3v-3H7a2 2 0 0 1-2-2V5a2 2 0 0 1 2-2z"/><circle cx="5" cy="16" r="2"/><circle cx="12" cy="17" r="2"/><circle cx="19" cy="16" r="2"/><path d="M2 22a3 3 0 0 1 6 0M9 22a3 3 0 0 1 6 0M16 22a3 3 0 0 1 6 0"/></svg></div>
    <h3>Public Affairs</h3>
    <p>Lorem ipsum dolor sit amet, consectetur adipiscing elit, sed do eiusmod tempor incididunt ut labore et dolore magna aliqua enim ad minim veniam.</p>
    <a class="btn" href="#">Know More</a>
  </article>

  <article class="service" style="left:810px">
    <div class="icon"><svg width="62" height="62" viewBox="0 0 24 24" fill="none" stroke="#fff" stroke-width="1.5" stroke-linecap="round"><rect x="5" y="3" width="14" height="9"/><circle cx="5" cy="15" r="2"/><circle cx="19" cy="15" r="2"/><path d="M2 22v-2a3 3 0 0 1 6 0v2M16 22v-2a3 3 0 0 1 6 0v2M8 9l3-3 2 2 3-3"/></svg></div>
    <h3>Marketing Communication</h3>
    <p>Lorem ipsum dolor sit amet, consectetur adipiscing elit, sed do eiusmod tempor incididunt ut labore et dolore magna aliqua enim ad minim veniam.</p>
    <a class="btn" href="#">Know More</a>
  </article>
</section>

<section class="news">
  <h2 class="heading">News</h2>
  <div class="arrow" style="left:90px"><svg width="16" height="16" viewBox="0 0 16 16"><path d="M10 3L5 8l5 5" fill="none" stroke="#fff" stroke-width="2.4"/></svg></div>
  <div class="arrow" style="left:1066px"><svg width="16" height="16" viewBox="0 0 16 16"><path d="M6 3l5 5-5 5" fill="none" stroke="#fff" stroke-width="2.4"/></svg></div>

  <article class="post" style="top:120px">
    <div class="thumb" role="img" aria-label="Photo of a news contributor"></div>
    <div class="body">
      <time>July 14, 2014</time>
      <h4>Lorem ipsum dolor sit amet Consectetur adipiscing</h4>
      <p>Sed ut perspiciatis unde omnis iste natus error sit voluptatem accusantium doloremque laudantium, totam rem aperiam eaque ipsa quae ab illo inventore veritatis et quasi architecto beatae vitae dicta sunt explicabo.</p>
      <div class="more">More</div>
    </div>
  </article>

  <article class="post" style="top:272px">
    <div class="thumb" role="img" aria-label="Photo of a news contributor"></div>
    <div class="body">
      <time>July 10, 2014</time>
      <h4>Lorem ipsum dolor sit amet Consectetur adipiscing</h4>
      <p>Sed ut perspiciatis unde omnis iste natus error sit voluptatem accusantium doloremque laudantium, totam rem aperiam eaque ipsa quae ab illo inventore veritatis et quasi architecto beatae vitae dicta sunt explicabo.</p>
      <div class="more">More</div>
    </div>
  </article>
</section>

<section class="contact">
  <div class="contact-photo" role="img" aria-label="Photo of a professional in a city setting, darkened"></div>
  <h2 class="heading">Contact Us</h2>
  <form class="form">
    <div class="field" style="top:0">Name</div>
    <div class="field" style="top:68px">Email</div>
    <div class="field" style="top:136px">Phone Number</div>
    <div class="message">Message</div>
    <div class="btn submit">Submit</div>
  </form>
</section>

<footer class="footer">
  <nav>
    <a href="#">Home</a><a href="#">About Us</a><a href="#">Services</a><a href="#">News</a><a href="#">Contact Us</a><a href="#">Privacy Policy</a>
  </nav>
  <div class="copy">© 2014 TORVEX Media. All Rights Reserved.</div>
  <div class="social"><span></span><span></span><span></span></div>
</footer>

</body>
</html>
```